WordPress design project for Brindlow Construction

Brindlow Construction, Inc. (www.brindlowinc.example) is a private organization. It is run by the same family that founded Brindlow Waste Systems (www.brindlow.example), a large, publicly-held waste management organization in the US. While owned by the same family, the two organizations are run independently.
Brindlow Construction is a well-established New England USA construction outfit specializing in site development, heavy excavation, aggregate, large-scale/municipal water and sewer systems, and landfill construction and closure. Brindlow Construction is not in any way a residential or commercial building contractor.
Brindlow Construction also operates hydraulic and hydrostatic service shops, as well as aggregate (gravel, sand, stone, top soil, and anything else aggregate) sites. Both are for more traditional, non-project customers, such as landscapers and other construction companies.
Business contact information is as noted below:
Address:
Brindlow Construction, Inc.
48 Quarry Row
Fairhollow, Vermont 05799
Telephone:
802-555-0148
Fax:
802-555-0193
Email:
info@brindlowinc.example
A tagline used in a recent advertisement was:
"Committed to providing a complete array of services for over 30 years, we are New England's premier construction company."
In reviewing design ideas internally, we found bits and pieces of the following sites appealing:
TR Construction (Wendermoor) - http://www.trconstruction.example/
Halvorsk Construction - http://www.halvorsk.example/
Pellow Construction - http://www.pellowconstruction.example/
Greyfield Construction Group - http://www.greyfieldconstructiongroup.example/
Varko Construction - http://www.varko.example/
Lindqvist Brothers Construction http://www.lindqvistbros.example/
Ormsby Construction http://www.ormsby-corp.example/
The blue in the logo is hex #00253f. The logo was designed by hand many years ago, so the font is unknown.
We would like a fresh, professional design that effectively illustrates what we do in a thoughtful, impressive way.
Target Market(s)
Would-be clients, land developers, waste organizations, energy developers, engineers, surveyors, landscapers, heavy equipment operators and the likes.
Industry/Entity Type
Waste Management
Requirements
Must have
- Lots of media capabilities, such as embedded video (via YouTube is fine), project image gallery, and sliders for various functions.
A large slider on the landing page is critical, as well as space for standard things, such as news/events, job opportunities, project highlights, and the likes.
We also want to highlight things like employee longevity. Some of our team have been with us since the beginning.
We need to add emphasis to the fact that our hydraulic/hydro static services and aggregate operations are for anyone who needs such service or material. Related, we need a place to set prices and descriptions of such material to help site visitors decide what they may need.
We need a place to highlight business partners, such as Felix Harrow and Ironbeetle.
We also need form capabilities for things like bid requests and general contacts from the public. Related, there should be social media capabilities.
Nice to have
- This is almost a must have, but we're open to options. The WordPress design should be capable of fitting into the very popular PlyFrames Trellis theme.

```html
<!DOCTYPE html>
<html lang="en">
<head>
<meta charset="utf-8">
<title>Brindlow Construction, Inc.</title>
<link href="https://fonts.googleapis.com/css2?family=Fjalla+One&family=Oswald:wght@700&family=Arimo:wght@400;700&display=swap" rel="stylesheet">
<style>
:root{
  --navy:#0a2c5a;
  --navy-deep:#00253f;
  --orange:#f5a623;
  --orange-soft:#fbd79a;
  --ink:#222;
  --body:#333;
  --link:#1b4f8a;
  --footer:#1b1b1b;
  --footer-text:#c9c9c9;
  --bottom-bar:#bdbdbd;
  --line:#d6d6d6;
}
*{margin:0;padding:0;box-sizing:border-box}
html,body{width:756px;height:1200px;overflow:hidden;background:#fff}
body{position:relative;font-family:"Arimo",Arial,sans-serif;color:var(--body)}
.abs{position:absolute}

.site-header{left:0;top:0;width:756px;height:120px;
  background:linear-gradient(180deg,#d9e0e7 0%,#eef1f4 60%,#e3e8ed 100%);border-top:4px solid #111}
.social-bar{left:546px;top:0;width:122px;height:26px;background:#111;border-radius:0 0 8px 8px;
  display:flex;gap:5px;justify-content:center;align-items:center}
.social-bar span{width:19px;height:19px;border-radius:50%;background:var(--orange)}
.brand{left:88px;top:42px;display:flex;align-items:center;gap:10px}
.brand-mark{width:44px;height:44px;background:var(--navy-deep)}
.brand-name{font-family:"Oswald",sans-serif;font-weight:700;font-size:28px;color:var(--navy-deep);line-height:1}
.contact-lines{right:88px;top:34px;text-align:right;font-size:12px;color:var(--ink);line-height:22px}
.contact-lines b{font-family:Georgia,serif;font-weight:400;font-size:19px;color:var(--navy-deep);margin-left:4px}
.search{left:516px;top:86px;width:152px;height:22px;display:flex;border:1px solid #ccc;background:#fff}
.search span{flex:1;font-size:8px;color:#666;padding:6px 7px}
.search b{width:20px;background:var(--orange);font-size:9px;color:#222;text-align:center;line-height:20px}

.main-nav{left:0;top:120px;width:756px;height:34px;background:var(--navy)}
.main-nav ul{list-style:none;display:flex;position:absolute;left:88px;top:0;height:34px}
.main-nav li{color:#fff;font-size:11px;line-height:34px;padding:0 22px;border-right:1px solid #1c4174}
.main-nav li.current{background:var(--orange);color:#222;padding:0 12px;height:24px;line-height:24px;margin:5px 22px 0 0;border:0}

.hero{left:88px;top:154px;width:580px;height:190px;
  background:linear-gradient(120deg,#3a7ed6 0%,#5b9be2 45%,#d89a24 70%,#f2b640 100%)}
.hero-shadow{left:88px;top:344px;width:580px;height:14px;
  background:radial-gradient(ellipse at top,rgba(0,0,0,.45),rgba(0,0,0,0) 70%)}
.hero-tagline{left:106px;top:188px;font-family:"Fjalla One",sans-serif;font-size:23px;line-height:27px;color:#fff;white-space:nowrap}

.h2{font-family:"Oswald",sans-serif;font-weight:700;font-size:21px;color:var(--ink);line-height:1}
.intro{left:88px;top:422px;width:362px;font-size:8.2px;line-height:11.2px}
.divider{left:88px;top:510px;width:360px;height:1px;background:var(--line)}

.gallery{left:88px;top:559px;width:358px;height:132px;border:1px solid var(--line);background:#f7f7f7}
.thumb{top:18px;width:100px;height:96px;border:1px solid #ccc}
.arrow{top:54px;width:0;height:0;border-top:10px solid transparent;border-bottom:10px solid transparent}

.news{left:88px;top:744px;width:192px;font-size:8.2px;line-height:11px;white-space:nowrap}
.news .date{color:var(--link);margin-top:4px}
.news .more{color:var(--link)}
.news .view-all{margin-top:10px;text-align:right;padding-right:20px;font-size:10px;color:var(--ink);text-decoration:underline}

.audit{left:310px;top:750px;width:139px;height:90px;padding:12px 11px;
  background:linear-gradient(135deg,var(--orange-soft),#fde8c4);font-size:8.4px;line-height:11px;color:#333}
.audit u{display:block;margin-top:8px;font-size:9.5px}

.quote{left:484px;top:420px;width:184px;height:208px;background:var(--navy);padding:10px 11px}
.quote p{color:#fff;font-size:8.4px;line-height:11px;margin-bottom:10px}
.field{background:#eee;border:1px solid #bbb;height:20px;font-size:8.4px;padding:5px 5px;margin:0 0 8px 0;color:#333}
.field.tall{height:54px}
.submit{display:block;margin:6px auto 0;width:60px;height:22px;background:var(--orange);border:2px solid #fff;
  font-family:"Oswald",sans-serif;font-size:12px;text-align:center;line-height:18px;color:#222}

.video{left:484px;top:676px;width:184px;height:154px;background:linear-gradient(180deg,#6a7680,#2f3335 60%,#1c1c1c)}
.video-bar{left:486px;top:820px;width:180px;height:3px;background:#555}
.video-bar i{display:block;width:62px;height:3px;background:#c33}

.partners{left:88px;top:892px;width:580px;height:80px;border:1px solid var(--line);border-left:0}
.partners-title{left:88px;top:892px}
.partner-badge{top:913px;height:38px}

.site-footer{left:0;top:1018px;width:756px;height:158px;background:var(--footer)}
.footer-col{top:1027px;list-style:none;font-size:8.4px;line-height:16.4px;color:var(--footer-text)}
.footer-col u{color:#fff}
.contact-head{left:512px;top:1028px;color:#fff;font-size:12px}
.contact-box{left:512px;top:1051px;width:156px;height:114px;background:var(--orange);padding:12px 12px;font-size:8.4px;line-height:11px;color:#222}
.bottom-bar{left:0;top:1176px;width:756px;height:24px;background:var(--bottom-bar);font-size:8.4px;color:#222;padding:7px 88px}
</style>
</head>
<body>

<header class="site-header abs"></header>
<div class="social-bar abs" aria-label="Social links"><span></span><span></span><span></span><span></span><span></span></div>
<div class="brand abs"><span class="brand-mark"></span><span class="brand-name">Brindlow Construction</span></div>
<div class="contact-lines abs">Telephone: <b>802-555-0148</b><br>Fax: <b>802-555-0193</b></div>
<div class="search abs"><span>Search</span><b>GO</b></div>

<nav class="main-nav abs">
  <ul>
    <li class="current">HOME</li>
    <li>WHO WE ARE</li>
    <li>WHAT WE DO</li>
    <li>WHERE WE ARE</li>
    <li style="border:0">NEWS</li>
  </ul>
</nav>

<div class="hero abs" role="img" aria-label="Yellow crane boom against a blue sky"></div>
<div class="hero-tagline abs">Committed to providing a complete<br>array of services for over 30 years,<br>we are New England's premier<br>construction company.</div>
<div class="hero-shadow abs"></div>

<h2 class="h2 abs" style="left:88px;top:390px;font-size:23px">Welcome to our website</h2>
<p class="intro abs">Sed sit amet bibendum est. Mauris vulputate lectus sit amet elementum posuere. Vivamus pharetra orci quis ullamcorper cursus. Aliquam pulvinar elit sed ante scelerisque, id feugiat sapien consequat. Lorem ipsum dolor sit amet, consectetur adipiscing elit. Etiam quis tortor quis turpis facilisis scelerisque quis non augue. Vestibulum mollis fringilla luctus. Praesent a sem at enim lobortis ultricies. Suspendisse posuere adipiscing pulvinar. Aenean in felis dui. Duis nec hendrerit turpis. Sed tristique lobortis orci, gravida posuere lacus vulputate in. Cras dui dolor, volutpat vitae nunc in, tempus ultricies risus.</p>
<div class="divider abs"></div>

<h2 class="h2 abs" style="left:88px;top:528px">Project Gallery</h2>
<div class="gallery abs">
  <span class="arrow abs" style="left:2px;border-right:10px solid #333"></span>
  <div class="thumb abs" style="left:19px;background:linear-gradient(135deg,#d8c3b0,#7a5a4a 60%,#2d4f8a)" role="img" aria-label="Students at a community event"></div>
  <div class="thumb abs" style="left:130px;background:linear-gradient(135deg,#cbb6a0,#e9e4df 50%,#3d4f9a)" role="img" aria-label="Volunteers sorting clothing"></div>
  <div class="thumb abs" style="left:241px;background:linear-gradient(180deg,#9db86a,#c9b08a 55%,#8a8a84)" role="img" aria-label="School building and courtyard"></div>
  <span class="arrow abs" style="left:344px;border-left:10px solid #333"></span>
</div>

<h2 class="h2 abs" style="left:88px;top:714px">News &amp; Events</h2>
<div class="news abs">
  <div class="date">June 16, 2013</div>
  <div>Suspendisse posuere adipiscing pulvinar. Aenean in<br>felis dui. Duis nec hendrerit turpis. Sed tristique<br>lobortis orci, gravida posuere June 16.<span class="more">Read more...</span></div>
  <div class="date" style="margin-top:6px">May 23, 2013</div>
  <div>Suspendisse posuere adipiscing pulvinar. Aenean in<br>felis dui. Duis nec hendrerit turpis. Sed tristique<br>lobortis orci, gravida posuere June 16.<span class="more">Read more...</span></div>
  <div class="view-all">View all</div>
</div>

<h2 class="h2 abs" style="left:310px;top:714px">Free waste audit</h2>
<div class="audit abs">Let our experts evaluate your business's unique waste streams and recommend a custom solution.<u>Click here</u></div>

<h2 class="h2 abs" style="left:484px;top:390px">Get a quote</h2>
<form class="quote abs">
  <p>We're experts at listening to the needs of your business or home and recommending a solution that fits your wallet.</p>
  <div class="field">Name</div>
  <div class="field">Email</div>
  <div class="field tall">Massage</div>
  <span class="submit">SUBMIT</span>
</form>

<h2 class="h2 abs" style="left:484px;top:648px">Video</h2>
<div class="video abs" role="img" aria-label="Embedded video of a dark timber building among trees"></div>
<div class="video-bar abs"><i></i></div>

<div class="partners abs"></div>
<svg class="partners-title abs" width="112" height="80" viewBox="0 0 112 80">
  <polygon points="0,0 86,0 112,40 86,80 0,80" fill="var(--navy-deep)"/>
  <text x="12" y="34" fill="#fff" font-family="Arimo,Arial,sans-serif" font-size="19">Our</text>
  <text x="12" y="60" fill="#fff" font-family="Arimo,Arial,sans-serif" font-size="19">Partners</text>
</svg>
<div class="partner-badge abs" style="left:214px;width:75px;border:1px solid #7aa;background:#f4f8f8"></div>
<div class="partner-badge abs" style="left:298px;width:92px;background:#2a2f6e"></div>
<div class="partner-badge abs" style="left:402px;width:55px;background:#f2d21a"></div>
<div class="partner-badge abs" style="left:472px;width:110px;background:#e8e8e8"></div>
<div class="partner-badge abs" style="left:606px;width:56px;background:#d41a1a"></div>

<footer class="site-footer abs"></footer>
<ul class="footer-col abs" style="left:88px"><li>Home</li><li>Who we are</li><li>What we do</li><li>Where we are</li><li>Services</li><li>Testimonials</li><li>News</li></ul>
<ul class="footer-col abs" style="left:196px"><li>Meet Your Local Provider</li><li>Online Billing</li><li>Voice Your Opinion</li><li>Job opportunities</li><li>Project highlights</li><li>Employ Satisfaction</li></ul>
<ul class="footer-col abs" style="left:350px"><li>Industries</li><li>Education</li><li>Food &amp; Retail</li><li>Hospitality</li><li>Industrial</li><li>Sustainability Services</li><li>Municipalities</li><li>Construction</li><li><u>View more</u></li></ul>
<div class="contact-head abs">Contact us</div>
<div class="contact-box abs">Address:<br>Brindlow Construction, Inc.<br>48 Quarry Row<br>Fairhollow, Vermont 05799<br><br>Email us:<br><u>info@brindlowinc.example</u></div>
<div class="bottom-bar abs">Copyright 2013 www.brindlowinc.example All Rights Reserved.</div>

</body>
</html>
```